Responsive Mobile Quorvo Jewelry Template

We need to adapt an existing Quorvo template to be 100% responsive and mobile friendly. Due to Quorvo rules, the template would need to be implemented only using HTML and CSS (no Javascript). The template design files and HTML/CSS files are required for this project. We prefer that it is implemented using a responsive framework such as Bootstrap.

An example of our current template can be found here (diamond only):
https://www.quorvo.example/itm/518203746291?ViewItem=&item=518203746291

And example of our template with an additional section for gemstone:
https://www.quorvo.example/itm/518203746837?ViewItem=&item=518203746837

We had also somewhat recently designed our Quorvo store landing page so some consistency with this would be desired:
http://www.quorvoshops.example/HalvrenDesignsLA

Please also refer to our website: https://halvrendesignsla.example/

Target Market(s)

Primarily women shopping for jewelry on Quorvo.

Industry/Entity Type

Jewelry

Coding

Coded - Design and coding required

Number of Pages Required

1 page

Font styles to use
Sans Serif

Requirements
Must have
• * A color scheme that fits with the existing template design.
• * REMOVE the product photo in the template.
• * Sections required for Description, Basic Details, and Diamond/Gemstone Details.
• * Please refer to https://pages.quorvo.example/sell/itemdescription/mobilefriendlyguidelines.html in particular, the template must use
Nice to have
• * Menu of links to other categories is desired in a mobile friendly way.
• * We are open to graphics for links to popular categories similar to those found on the store page.
• * Implemented using a standardized responsive framework such as Bootstrap.

```html
<!DOCTYPE html>
<html lang="en">
<head>
<meta charset="utf-8">
<title>Diamond Split Shank Engagement Ring</title>
<link href="https://fonts.googleapis.com/css2?family=Roboto:wght@400;500;700&display=swap" rel="stylesheet">
<style>
:root{
  --bg:#ffffff;
  --text:#333333;
  --heading:#2b2b2b;
  --band:#f3e6fb;
  --link:#2f73b3;
  --rule:#dddddd;
  --metal-light:#f7f8fa;
  --metal-mid:#dde1e6;
}
*{margin:0;padding:0;box-sizing:border-box}
html,body{width:1200px;height:2467px;overflow:hidden;background:var(--bg)}
body{font-family:"Roboto",Arial,sans-serif;color:var(--text);position:relative}
.listing{position:absolute;left:100px;top:0;width:1000px}
.section-band{position:absolute;left:0;width:1000px;height:100px;background:var(--band);
  display:flex;align-items:center;padding-left:17px;font-size:46px;font-weight:700;color:var(--heading)}
.band-description{top:153px}
.band-questions{top:1737px}
.band-details{top:2020px}
.description-text{position:absolute;top:250px;left:0;width:1000px;font-size:48px;letter-spacing:0.8px;line-height:67px;color:var(--text);white-space:nowrap}
.product-visual{position:absolute;top:700px;left:50px;width:900px;height:700px;
  background:radial-gradient(ellipse 50% 40% at 50% 48%,var(--metal-mid) 0%,var(--metal-light) 55%,var(--bg) 100%)}
.more-link{position:absolute;top:1600px;left:0;width:1000px;text-align:center;font-size:50px;line-height:70px;font-weight:700;color:var(--link);text-decoration:none;white-space:nowrap}
.ask-line{position:absolute;top:1869px;left:50px;display:flex;align-items:center;gap:22px;font-size:47px;color:var(--link)}
.ask-line svg{width:53px;height:40px}
.details-table{position:absolute;top:2117px;left:0;width:1000px;border-collapse:collapse;font-size:46px;letter-spacing:0.3px;color:var(--text)}
.details-table td{height:70px;border-bottom:2px solid var(--rule);padding:0;vertical-align:middle;white-space:nowrap}
.details-table .label{width:402px}
</style>
</head>
<body>
<main class="listing">
  <div class="section-band band-description">Item Description</div>
  <p class="description-text">Classic Diamond Split Shank Engagement Ring<br>With 0.70 Carats Of Round Brilliants Set In 14k<br>White Gold</p>
  <div class="product-visual" role="img" aria-label="Product image: white gold split shank engagement ring with a round diamond cluster centre and pavé diamond bands"></div>
  <a class="more-link" href="#">Click Here to View Our Other Diamond<br>Rings!</a>
  <div class="section-band band-questions">Questions?</div>
  <div class="ask-line">
    <svg viewBox="0 0 32 24" aria-hidden="true"><rect x="1" y="1" width="30" height="22" fill="none" stroke="#111" stroke-width="2"/><path d="M1 1 L16 14 L31 1 M1 23 L12 11 M31 23 L20 11" fill="none" stroke="#111" stroke-width="2"/></svg>
    <span>Ask a question via email</span>
  </div>
  <div class="section-band band-details">Item Details</div>
  <table class="details-table">
    <tr><td class="label">Model Number:</td><td>HDL-KR48213WEB-ER</td></tr>
    <tr><td class="label">Metal:</td><td>14k White Gold</td></tr>
    <tr><td class="label">Weight:</td><td>3.2 grams</td></tr>
    <tr><td class="label">L x W x H:</td><td>7.6 x 19.5 x 6.8 MM</td></tr>
    <tr><td class="label">Style:</td><td>Cocktail</td></tr>
  </table>
</main>
</body>
</html>
```